Introduction of new dentist and new treatments

We want inform our Patients of our new dentist and new treatment methods. It is dealing about biologic dentistry and holistic dentistry. we are in switzerland and speak german

Font styles to use
Sans Serif

Colors
00a990
33b8a4
9bcb3c
acd036
cadf82
0292cd
3176b5
e34297
e667a6

Requirements
Must have
• Text, which can be edited. It will be in german
• Name of the dental clinic is
• "Velmora - Ihr Zahnarzt in Zug"
Nice to have
• A4 Layout

```html
<!DOCTYPE html>
<html lang="de">
<head>
<meta charset="utf-8">
<title>Velmora – Ihre Zahnärzte in Zug</title>
<link href="https://fonts.googleapis.com/css2?family=Source+Sans+3:wght@400;500;600&family=Tinos:wght@400&display=swap" rel="stylesheet">
<style>
  :root {
    --navy: #1b3462;
    --navy-text: #1f2f5c;
    --title-blue: #2a6fb8;
    --wave-blue: #3f86c9;
    --wave-light: #a9dbe6;
    --ring: #3e4a75;
    --paper: #f1f7f8;
    --body-grey: #555a62;
    --accent-pink: #e98aa6;
    --accent-aqua: #8fd3e3;
  }
  * { margin: 0; padding: 0; box-sizing: border-box; }
  html, body { width: 951px; height: 1200px; overflow: hidden; background: var(--paper); }
  body { font-family: "Source Sans 3", Arial, sans-serif; color: var(--body-grey); position: relative; }

  .hero { position: absolute; left: 0; top: 0; width: 951px; height: 560px; }
  .hero svg { display: block; }

  .brand { position: absolute; left: 26px; top: 382px; }
  .brand-name {
    font-family: "Source Sans 3", Arial, sans-serif;
    font-size: 42px; font-weight: 600; letter-spacing: 0; color: var(--navy-text); line-height: 1;
  }
  .brand-tagline {
    font-size: 18px; font-weight: 600; color: var(--navy-text);
    margin-top: 8px;
  }

  .headline {
    position: absolute; top: 540px; left: 30px; width: 891px; text-align: center;
    font-family: "Tinos", "Times New Roman", serif; font-size: 26px; line-height: 31px;
    color: var(--title-blue); font-weight: 400;
  }
  .intro {
    position: absolute; top: 614px; left: 48px; width: 860px;
    font-size: 17.5px; line-height: 20.5px; color: var(--navy-text); font-weight: 500;
  }

  .topic { position: absolute; width: 436px; }
  .topic-head { display: flex; align-items: center; gap: 8px; height: 36px; margin-bottom: 9px; }
  .topic-icon { width: 38px; height: 36px; flex: none; }
  .topic-title { font-size: 17px; line-height: 17px; color: var(--navy-text); font-weight: 400; }
  .topic-text {
    font-size: 13.8px; line-height: 15.6px; text-align: justify; hyphens: auto;
  }
  .topic-kauorgan { left: 26px; top: 688px; }
  .topic-parodontitis { left: 490px; top: 684px; }
  .topic-zahnverlust { left: 24px; top: 926px; }
  .topic-ganzheitlich { left: 490px; top: 926px; }

  .contact-bar {
    position: absolute; left: 0; top: 1117px; width: 951px; height: 83px;
    background: var(--navy); border-top: 5px solid var(--wave-light);
    display: flex; align-items: center; justify-content: space-between; padding: 0 33px 0 26px;
    color: #fff; font-size: 16.5px;
  }
  .contact-item { display: flex; align-items: center; gap: 9px; }
  .contact-item svg { width: 18px; height: 18px; }
</style>
</head>
<body>

<header class="hero">
  <svg width="951" height="560" viewBox="0 0 951 560">
    <defs>
      <linearGradient id="heroPhoto" x1="0" y1="0" x2="1" y2="0.4">
        <stop offset="0" stop-color="#dcebc4"/>
        <stop offset="0.35" stop-color="#f3f4ec"/>
        <stop offset="0.6" stop-color="#d9b49c"/>
        <stop offset="1" stop-color="#f4efe9"/>
      </linearGradient>
      <linearGradient id="portraitFill" x1="0" y1="0" x2="0" y2="1">
        <stop offset="0" stop-color="#eef0f2"/>
        <stop offset="0.55" stop-color="#d8ab90"/>
        <stop offset="1" stop-color="#2f74c0"/>
      </linearGradient>
    </defs>
    <rect x="0" y="0" width="951" height="480" fill="url(#heroPhoto)" role="img" aria-label="Foto einer lächelnden jungen Frau mit gesunden Zähnen"/>
    <path d="M0 240 C130 190 300 230 390 290 C450 330 470 400 560 430 C680 465 820 420 951 380 L951 560 L0 560 Z" fill="#ffffff"/>
    <path d="M0 470 C180 500 330 480 470 440 C620 395 760 390 951 420 L951 450 C780 420 640 430 500 470 C350 512 180 520 0 500 Z" fill="var(--wave-blue)"/>
    <path d="M0 500 C180 520 350 512 500 470 C640 430 780 420 951 450 L951 475 C790 445 660 460 520 495 C360 535 180 540 0 520 Z" fill="var(--wave-light)"/>
    <path d="M0 520 C180 540 360 535 520 495 C660 460 790 445 951 475 L951 560 L0 560 Z" fill="var(--paper)"/>
    <circle cx="811" cy="410" r="103" fill="var(--ring)"/>
    <circle cx="811" cy="410" r="90" fill="url(#portraitFill)" role="img" aria-label="Porträtfoto des neuen Zahnarztes"/>
  </svg>
  <div class="brand">
    <div class="brand-name">Velmora</div>
    <div class="brand-tagline">Ihre Zahnärzte in Zug</div>
  </div>
</header>

<h1 class="headline">Interdisziplinäre Zahnmedizin - Zusammenhang zwischen Zahnproblemen<br>und der Gesundheit von Körper und Geist</h1>

<p class="intro">Zahn und Gesundheit haben eins gemeinsam – Man vermisst sie, wenn sie fehlt. Zähne haben einen engen Zusammenhang zur Gesundheit und können diese beeinflussen. Sowohl negativ als auch positiv.</p>

<section class="topic topic-kauorgan">
  <div class="topic-head">
    <svg class="topic-icon" viewBox="0 0 38 36"><circle cx="14" cy="16" r="9" fill="none" stroke="var(--accent-pink)" stroke-width="3"/><line x1="8" y1="23" x2="2" y2="30" stroke="var(--accent-pink)" stroke-width="3" stroke-linecap="round"/><circle cx="29" cy="18" r="7" fill="var(--accent-aqua)"/></svg>
    <h2 class="topic-title">Funktion des Kauorgans<br>und interdisziplinäre Zahnmedizin</h2>
  </div>
  <p class="topic-text">„Funktion ist nicht alles. Aber ohne Funktion ist alles nichts!“ Sagte einst Prof. A. Lindqvist (Zahnarzt, Gnathologie) und betonte die Bedeutung der Funktion des Kausystems. Sprechen, Kauen aber auch Körperhaltung und Stressmanagement gehören zu den Funktionen der Zähne. Ein gut funktionierendes Kauorgan (nach Prof. R. Hartmann, interdisziplinäre Zahnmedizin) kann Stress bewältigen und mehr Leistung und Wohlbefinden bringen. Sehr oft erkennt man Funktionsstörungen daran, dass die Zähne nicht richtig zueinander passen oder Muskelverspannungen und Schmerzen im Kiefergelenk auftreten.</p>
</section>

<section class="topic topic-parodontitis">
  <div class="topic-head">
    <svg class="topic-icon" viewBox="0 0 38 36"><rect x="4" y="20" width="26" height="12" rx="3" fill="var(--accent-pink)"/><circle cx="17" cy="14" r="9" fill="var(--accent-aqua)"/></svg>
    <h2 class="topic-title">Parodontitis und<br>systemische Erkrankungen</h2>
  </div>
  <p class="topic-text">Parodontitis (Entzündung des Zahnhalteapparats) ist eine der häufigsten chronischen Krankheiten weltweit und daher gut erforscht. Herzkrankheiten, Diabetes und Frühgeburtlichkeit sind einige der systemischen Krankheiten mit der Parodontitis in Zusammenhang steht. Zahnfleischbluten, Zahnlockerung, Zahnfleischschwund und Zahnverlust sind typische Begleiterscheinungen von Parodontitis. Eine systematische Parodontitis-Behandlung kann auch positive Auswirkungen auf die gesamte Gesundheit haben.</p>
</section>

<section class="topic topic-zahnverlust">
  <div class="topic-head">
    <svg class="topic-icon" viewBox="0 0 38 36"><circle cx="17" cy="16" r="10" fill="var(--accent-aqua)"/><circle cx="21" cy="11" r="4" fill="var(--accent-pink)"/></svg>
    <h2 class="topic-title">Zahnverlust und<br>neurologische Auswirkung</h2>
  </div>
  <p class="topic-text">Ein physiologisches Kausystem hat sehr feine Steuerungs- und Wahrnehmungsmöglichkeiten. Bei Zahnverlust werden diese Fähigkeiten weniger benötigt. Weniger gebrauchte Ressourcen werden von der Natur dementsprechend abgebaut. Studien zeigen, dass Menschen mit weniger Zähnen mehr Risiko zur Bildung von Demenz bergen.</p>
</section>

<section class="topic topic-ganzheitlich">
  <div class="topic-head">
    <svg class="topic-icon" viewBox="0 0 38 36"><circle cx="18" cy="20" r="11" fill="var(--accent-aqua)"/><circle cx="22" cy="7" r="3" fill="var(--accent-pink)"/></svg>
    <h2 class="topic-title">Ganzheitliche Erklärungen</h2>
  </div>
  <p class="topic-text">Die komplementäre Zahnheilkunde, sehr oft auch als ganzheitliche oder biologische Zahnheilkunde bezeichnet, versucht mit Hilfe von Meridianen (Traditionelle Chinesische Medizin), den Zusammenhang zwischen Zähnen und anderen Organen und Körperteilen zu erklären. Es gibt immer mehr Patienten und Zahnärzte die von dieser Theorie und deren Ergebnissen überzeugt sind. Aufgrund der wissenschaftlichen Lage ist eine ausführliche Aufklärung vor der Behandlung sehr ratsam.</p>
</section>

<footer class="contact-bar">
  <div class="contact-item">
    <svg viewBox="0 0 18 18"><path d="M9 1a6 6 0 0 0-6 6c0 4.5 6 10 6 10s6-5.5 6-10a6 6 0 0 0-6-6z" fill="#fff"/><circle cx="9" cy="7" r="2.2" fill="var(--navy)"/></svg>
    <span>Zahnarztpraxis Seestrasse 18, 6300 Zug</span>
  </div>
  <div class="contact-item">
    <svg viewBox="0 0 18 18"><circle cx="9" cy="9" r="7.5" fill="none" stroke="#fff" stroke-width="1.5"/><path d="M6.2 5.2l1.5-.3.8 2-1 .8a5 5 0 0 0 2.8 2.8l.8-1 2 .8-.3 1.5c-3.5.3-6.9-3.1-6.6-6.6z" fill="#fff"/></svg>
    <span>+41 41 555 01 23</span>
  </div>
  <div class="contact-item">
    <svg viewBox="0 0 18 18" fill="none" stroke="#fff" stroke-width="1.3"><circle cx="9" cy="9" r="7.5"/><ellipse cx="9" cy="9" rx="3.2" ry="7.5"/><line x1="1.5" y1="9" x2="16.5" y2="9"/><line x1="3" y1="5" x2="15" y2="5"/><line x1="3" y1="13" x2="15" y2="13"/></svg>
    <span>www.velmora-zug.ch</span>
  </div>
</footer>

</body>
</html>
```